Marlowe Brisa Pale Ale Beer Label/Badge

We need a Beer Label designed for our first official beer to be launched under the Marlowe Brand!!
It will be a Pale Ale Called "Brisa Pale Ale"!

The Marlowe has the largest Craft Beer & Cider selection in the Geelong & Surf Coast region. With a funky location and a relaxed vibe, Marlowe prides itself on serving delicious, unique seasonal food paired with Australia's best Craft Beer. The marlowe is the perfect setting for a relaxed afternoon or evening with friends and can package an experience for larger groups or corporate bookings.

The Marlowe Tavern brand has been growing for over a year and a half and the first label needs to integrate the Marlowe Logo but at the same time bring a fresh, new and eye catching feel to it along with embracing the "Odysseus" story in which we will be naming future beers.

The story of Calypso is found via the following link
http://en.lorevault.example/wiki/Brisa_(legend)

We expect designers to research the Marlowe Tavern brand along with the all important Craft Beer Market and demographics. This will, potentially, be the start of many more labels to come for the winning designer!!

Requirements
Must have
• The original "O" needs to be integrated into the new logo and as much as the Greek mythology is being used it needs to be certain that this is an original Australian Craft Beer in the modern age!!
strong, modern & unique!!
Nice to have
• Logo could have a depiction of Calypso
Should not have
• tackiness or cheap!!

```html
<!DOCTYPE html>
<html lang="en">
<head>
<meta charset="utf-8">
<title>Marlowe Brisa Pale Ale – Label Set</title>
<link rel="stylesheet" href="https://fonts.googleapis.com/css2?family=Krona+One&family=Quantico:wght@700&family=Montserrat:wght@500;800&display=swap">
<style>
  :root {
    --paper: #ffffff;
    --sand: #d4cb96;
    --rust: #d65a2c;
    --label-beige: #c9bda4;
    --frame-brown: #5a3b1c;
    --brand-red: #9e2a26;
    --name-grey: #58544f;
    --ink: #141414;
    --art-sun: #b49a55;
    --art-sky: #8f8b66;
    --art-sea: #3f68a8;
  }
  html, body {
    margin: 0;
    padding: 0;
    overflow: hidden;
  }
  body {
    width: 1200px;
    height: 1019px;
    background: var(--paper);
    position: relative;
  }
  .neck-band, .front-label {
    position: absolute;
    display: block;
  }
  .neck-band { width: 428px; height: 139px; top: 69px; }
  .neck-band--sand { left: 86px; --ground: var(--sand); }
  .neck-band--rust { left: 676px; --ground: var(--rust); }

  .front-label { width: 573px; height: 685px; top: 283px; }
  .front-label--sand { left: 13px; --ground: var(--sand); --foot-ink: var(--ink); }
  .front-label--rust { left: 613px; --ground: var(--rust); --foot-ink: #ffffff; }

  .ground { fill: var(--ground); }
  .panel { fill: var(--label-beige); stroke: var(--frame-brown); stroke-width: 10; }
  .stripe { fill: var(--frame-brown); }
  .brand-dot { fill: var(--brand-red); }
  .brand-name-small {
    font-family: "Quantico", sans-serif; font-weight: 700;
    fill: var(--brand-red); font-size: 16px; letter-spacing: 1px;
  }
  .arc-caption {
    font-family: "Montserrat", sans-serif; font-weight: 500;
    font-size: 10px; letter-spacing: 1.5px; fill: var(--ink);
  }
  .brand-name {
    font-family: "Quantico", sans-serif; font-weight: 700;
    font-size: 42px; letter-spacing: 2px; fill: var(--name-grey);
  }
  .brand-sub {
    font-family: "Montserrat", sans-serif; font-weight: 500;
    font-size: 14px; letter-spacing: 2.5px; fill: var(--name-grey);
  }
  .beer-name {
    font-family: "Krona One", sans-serif;
    font-size: 58px; letter-spacing: 4px;
    fill: #ffffff; stroke: var(--ink); stroke-width: 7;
    paint-order: stroke; stroke-linejoin: round;
  }
  .style-letter {
    font-family: "Montserrat", sans-serif; font-weight: 800;
    font-size: 20px; fill: var(--ink);
  }
  .rule { stroke: var(--name-grey); stroke-width: 1; }
  .abv {
    font-family: "Montserrat", sans-serif; font-weight: 500;
    font-size: 14px; letter-spacing: 1px; fill: var(--ink);
  }
  .origin {
    font-family: "Montserrat", sans-serif; font-weight: 500;
    font-size: 11px; letter-spacing: 1px; fill: var(--foot-ink);
  }
</style>
</head>
<body>

<svg width="0" height="0" style="position:absolute" aria-hidden="true">
  <defs>
    <linearGradient id="art-tone" x1="0" y1="0" x2="0" y2="1">
      <stop offset="0" stop-color="var(--art-sky)"/>
      <stop offset="0.45" stop-color="var(--art-sun)"/>
      <stop offset="0.82" stop-color="#7a6a5a"/>
      <stop offset="0.84" stop-color="var(--art-sea)"/>
      <stop offset="1" stop-color="#2f5592"/>
    </linearGradient>

    <symbol id="band" viewBox="0 0 428 139">
      <rect class="ground" width="428" height="139"/>
      <rect x="0" y="9" width="428" height="121" fill="var(--label-beige)"/>
      <rect class="stripe" x="0" y="9" width="428" height="12"/>
      <rect class="stripe" x="0" y="118" width="428" height="12"/>
      <circle class="brand-dot" cx="170" cy="69" r="13"/>
      <text class="brand-name-small" x="192" y="75">MARLOWE</text>
    </symbol>

    <symbol id="label" viewBox="0 0 573 685">
      <rect class="ground" width="573" height="685"/>
      <path class="panel" d="M31 103 H200 A88 88 0 0 1 376 103 H544 V637 H31 Z"/>
      <path id="arc-line" d="M220 103 A68 68 0 0 1 356 103" fill="none"/>
      <text class="arc-caption"><textPath href="#arc-line" startOffset="50%" text-anchor="middle">HANDCRAFTED BEER</textPath></text>
      <circle class="brand-dot" cx="288" cy="95" r="14"/>
      <text class="brand-name" x="288" y="187" text-anchor="middle">MARLOWE</text>
      <text class="brand-sub" x="288" y="205" text-anchor="middle">TAVERN + BREWERY</text>
      <rect x="60" y="234" width="457" height="255" fill="url(#art-tone)" stroke="#8a7a4a" stroke-width="2"
            role="img" aria-label="Label artwork"/>
      <text class="beer-name" x="288" y="550" text-anchor="middle">BRISA</text>
      <g class="style-row">
        <text class="style-letter" x="71" y="584" text-anchor="middle">P</text>
        <text class="style-letter" x="125" y="584" text-anchor="middle">A</text>
        <text class="style-letter" x="184" y="584" text-anchor="middle">L</text>
        <text class="style-letter" x="232" y="584" text-anchor="middle">E</text>
        <circle class="brand-dot" cx="287" cy="577" r="10"/>
        <text class="style-letter" x="347" y="584" text-anchor="middle">A</text>
        <text class="style-letter" x="423" y="584" text-anchor="middle">L</text>
        <text class="style-letter" x="507" y="584" text-anchor="middle">E</text>
      </g>
      <line class="rule" x1="60" y1="606" x2="230" y2="606"/>
      <line class="rule" x1="345" y1="606" x2="515" y2="606"/>
      <text class="abv" x="288" y="611" text-anchor="middle">ABV 5%</text>
      <text class="origin" x="288" y="659" text-anchor="middle">Kestrel Ridge, Victoria, Australia</text>
    </symbol>
  </defs>
</svg>

<svg class="neck-band neck-band--sand" viewBox="0 0 428 139" role="img" aria-label="Neck band, sand edition"><use href="#band"/></svg>
<svg class="neck-band neck-band--rust" viewBox="0 0 428 139" role="img" aria-label="Neck band, rust edition"><use href="#band"/></svg>

<svg class="front-label front-label--sand" viewBox="0 0 573 685" role="img" aria-label="Marlowe Brisa Pale Ale front label, sand edition"><use href="#label"/></svg>
<svg class="front-label front-label--rust" viewBox="0 0 573 685" role="img" aria-label="Marlowe Brisa Pale Ale front label, rust edition"><use href="#label"/></svg>

</body>
</html>
```